Real Estate agent needs flyer/folder to contain bio and overview of services

I'm including files of the layout of the small folder. The folder is 6 1/2 across and 9 1/2 inches long. It will have a front & back cover and then writing on the 2 inside pages.

I am sending a few files to incorporate into the flyer, 1 new logo to use and 2 files which are coloring ideas.

```html
<!DOCTYPE html>
<html lang="en">
<head>
<meta charset="utf-8">
<title>Inside 2 Pages – Agent Folder</title>
<link rel="stylesheet" href="https://fonts.googleapis.com/css2?family=Source+Serif+4:ital,opsz,wght@0,8..60,400;0,8..60,700;1,8..60,700&family=Ubuntu:wght@400&family=Passion+One:wght@700&family=Poppins:wght@700&family=Open+Sans:wght@400&display=swap">
<style>
  :root {
    --ink: #1c1c1c;
    --royal: #1f4fa8;
    --navy-box: #1c1ea0;
    --deep-blue: #13208f;
    --heading-blue: #1a3a9c;
    --cyan: #4fe6e8;
    --you-cyan: #49e0d8;
    --you-grey: #a9a898;
    --link-blue: #2060c8;
    --quote-grey: #5b5b5b;
    --tenet-grey: #ececec;
    --frame: #222;
    --card-border: #c8c8c8;
  }
  * { box-sizing: border-box; margin: 0; padding: 0; }
  html, body { width: 1200px; height: 923px; overflow: hidden; background: #fff; }
  body { position: relative; font-family: "Source Serif 4", Georgia, serif; color: var(--ink); }
  .abs { position: absolute; }

  .sheet-title { left: 0; width: 1200px; top: -8px; text-align: center; font-size: 39px; font-weight: 400; }

  .frame { left: 0; top: 0; width: 1200px; height: 923px; }

  /* Left page */
  .portrait { left: 140px; top: 56px; width: 136px; height: 170px; background: linear-gradient(180deg, #e9dcc7 0%, #d9b98a 45%, #2a2a2a 100%); border-radius: 2px; }
  .greeting { left: 18px; top: 226px; width: 352px; height: 105px; background: var(--royal); border-radius: 0 40px 6px 6px; }
  .greeting-hi { left: 74px; top: 218px; font-family: "Passion One", sans-serif; font-weight: 700; font-size: 100px; color: #fff; line-height: 1; transform: scaleX(0.74); transform-origin: left top; }
  .greeting-name { left: 182px; top: 246px; font-family: "Ubuntu", sans-serif; font-size: 26.5px; line-height: 34px; color: #fff; white-space: nowrap; }

  .bio { left: 386px; top: 154px; width: 197px; font-size: 11.4px; line-height: 15.2px; letter-spacing: -0.15px; text-align: justify; }
  .bio p + p { margin-top: 15px; }

  .tenet-label { left: 53px; top: 358px; width: 115px; height: 95px; background: var(--tenet-grey); padding: 26px 0 0 17px; font-size: 19px; line-height: 24px; }
  .tenet-you { left: 168px; top: 358px; width: 181px; height: 95px; background: var(--deep-blue); color: #fff; }
  .tenet-you .lead { position: absolute; left: 14px; top: 7px; font-size: 16px; }
  .tenet-you .big { position: absolute; left: 13px; top: 22px; font-family: "Poppins", sans-serif; font-weight: 700; font-size: 66px; line-height: 1; letter-spacing: -1px; }
  .big .y, .big .u { color: var(--you-cyan); }
  .big .o { color: var(--you-grey); }
  .tenet-text { left: 54px; top: 458px; width: 294px; font-size: 12px; line-height: 15.2px; text-align: justify; }
  .tenet-text em { color: var(--link-blue); font-weight: 700; }

  .services-title { left: 26px; width: 556px; top: 564px; text-align: center; font-size: 21px; font-weight: 700; color: var(--heading-blue); }
  .services-box { left: 26px; top: 597px; width: 555px; height: 306px; background: var(--navy-box); border: 1px solid #0d0f60; }
  .svc { position: absolute; right: 6px; color: #fff; font-size: 11px; line-height: 12.8px; text-align: justify; }
  .svc-head { position: absolute; left: 38px; top: 91px; font-size: 21px; font-weight: 700; color: var(--cyan); }

  /* Right page */
  .buying-small { left: 658px; top: 100px; font-size: 19px; font-weight: 700; color: #2f3d6a; }
  .buying-big { left: 664px; top: 122px; font-family: "Passion One", sans-serif; font-weight: 700; font-size: 50px; line-height: 1; color: var(--deep-blue); transform: scaleX(0.82); transform-origin: left top; }
  .home-photo { left: 784px; top: 84px; width: 272px; height: 143px; background: linear-gradient(180deg, #2a2f52 0%, #5a4a3a 45%, #2f77c8 80%, #8ab9e6 100%); }
  .buying-copy { left: 648px; top: 237px; width: 467px; font-size: 11.6px; line-height: 15px; letter-spacing: -0.1px; text-align: justify; }
  .buying-copy p + p { margin-top: 15px; }

  .testimonials-title { left: 800px; width: 196px; top: 481px; text-align: center; font-size: 23px; font-weight: 700; color: var(--heading-blue); }
  .quote-mark { font-family: "Passion One", sans-serif; font-size: 92px; line-height: 1; color: var(--quote-grey); }
  .card { border: 1px solid var(--card-border); background: #fff; padding: 4px 6px 0 7px; font-size: 12px; line-height: 15.1px; }
  .card strong { font-style: italic; }
  .card .who { margin-top: 14px; font-family: "Open Sans", sans-serif; font-size: 11.8px; color: var(--link-blue); }
</style>
</head>
<body>
  <h1 class="abs sheet-title">Inside 2 Pages</h1>

  <svg class="abs frame" viewBox="0 0 1200 923" aria-hidden="true">
    <defs>
      <linearGradient id="edgeTint" x1="0" y1="0" x2="1" y2="0">
        <stop offset="0" stop-color="#bfeefa"/>
        <stop offset="1" stop-color="#5fc9f0"/>
      </linearGradient>
    </defs>
    <path d="M1060,46 Q1290,490 1128,922 L1200,922 L1200,46 Z" fill="url(#edgeTint)" opacity=".75" role="img" aria-label="Faint blue geometric triangle pattern along the right edge"/>
    <line x1="142" y1="46" x2="1200" y2="46" stroke="var(--frame)" stroke-width="1"/>
    <line x1="144" y1="922" x2="1200" y2="922" stroke="var(--frame)" stroke-width="1"/>
    <line x1="600" y1="46" x2="600" y2="922" stroke="var(--frame)" stroke-width="1.2"/>
    <path d="M142,46 Q-140,484 144,922" fill="none" stroke="var(--frame)" stroke-width="1"/>
    <path d="M1060,46 Q1290,490 1128,922" fill="none" stroke="var(--frame)" stroke-width="1"/>
  </svg>

  <!-- Left page -->
  <div class="abs portrait" role="img" aria-label="Portrait photograph of the agent in a dark blazer"></div>
  <div class="abs greeting"></div>
  <div class="abs greeting-hi">HI!</div>
  <div class="abs greeting-name">It's me<br>Dana Whitford</div>

  <div class="abs bio">
    <p>I'm originally from Chicago, but I'm a full-fledged California girl now. I've lived and worked in Orange County since 1996. I always say where we live is the next best thing to living on a tropical island. I've traveled to many and I'm always happy to come back to my Laguna Niguel home.</p>
    <p>My passion for this area is why I'm in Real Estate. I consider myself incredibly fortunate to sell homes and help people purchase homes in an area that I love with all my heart.</p>
    <p>This passion also carries over in representing my clients with the highest degree of professionalism, enthusiasm and care. My business is built on exceptional customer service and I'm grateful my clients are mostly repeat and referrals.</p>
  </div>

  <div class="abs tenet-label">My<br>Core Tenet</div>
  <div class="abs tenet-you">
    <span class="lead">It's all about</span>
    <span class="big"><span class="y">Y</span><span class="o">O</span><span class="u">U</span></span>
  </div>
  <p class="abs tenet-text">My #1 priority is understanding <b>YOUR</b> <em>needs</em> and <b>YOUR</b> <em>objectives</em>. This understanding, along with working diligently on your behalf, means we accomplish your goal whether you're purchasing your 1st home or selling a home you've loved so you can move on to the next chapter of your life.</p>

  <h2 class="abs services-title">Real Estate Services &amp; Beyond...</h2>
  <div class="abs services-box">
    <p class="svc" style="left:12px;top:12px;">Simply put, I help people who are local, relocating and investing, sell and purchase homes in Southern California. For purchases outside of California, I can refer to a network of agents across the country.</p>
    <p class="svc" style="left:24px;top:55px;">I also provide a team who is dedicated to providing outstanding customer service throughout the transaction. My team includes a network of lenders, title, and escrow officers, in house CPA, stagers, photographers, contractors and more.</p>
    <h3 class="svc-head">Selling your home...</h3>
    <p class="svc" style="left:46px;top:121px;">Selling your home is not like any other business transaction. It's also personal. My priority as your Listing Agent is to guide you through what can be a complicated and sometimes emotional process.</p>
    <p class="svc" style="left:62px;top:163px;">I place great emphasis on marketing your property with professional photographs, along with harnessing the power of the Internet and the virtual world to reach as many buyers as possible. Your property will be marketed to the public as well as to other agents, thus creating maximum exposure of your home.</p>
    <p class="svc" style="left:95px;top:231px;">When we first meet to discuss selling your home, it's essential for me to gain an understanding of your unique needs such as time lines, expectations and financial considerations, just to name a few. From there, I begin the process of listing and marketing your home. I lead you through negotiations and more paperwork than you ever care to do, guiding you to the successful closing of your home.</p>
  </div>

  <!-- Right page -->
  <div class="abs buying-small">Buying a</div>
  <div class="abs buying-big">HOME</div>
  <div class="abs home-photo" role="img" aria-label="Evening photograph of a luxury home with a lit pool, framed by a white house outline"></div>

  <div class="abs buying-copy">
    <p>If you're thinking about buying a home, it's imperative you have an accomplished, real estate professional by your side to walk you through what is likely the largest purchase of your life.</p>
    <p>To get started, I like to meet with you so we have an opportunity to get to know each other as purchasing a home is a uniquely, personal endeavor. At that time, we can discuss your goals and if it's a good time for you to purchase a home.</p>
    <p>From there, the first step is to obtain a pre-approval from a lender. I'm able to recommend various lenders who can introduce and explain the various loan products available.</p>
    <p>After you've been pre-approved, that's when the fun starts! I guide you through the home buying adventure every step of the way and look forward to handing you the keys to your new home.</p>
  </div>

  <h2 class="abs testimonials-title">Testimonials</h2>
  <div class="abs quote-mark" style="left:624px;top:488px;">“</div>
  <div class="abs quote-mark" style="left:1118px;top:688px;">”</div>

  <div class="abs card" style="left:642px;top:526px;width:165px;height:355px;">
    <p>During the home buying process, Dana becomes your trusted advisor, mentor and friend. <strong>Her knowledge of the industry, community and market are best in class.</strong> A true professional! Dana aligned her goals with my own and understood the motivation behind my purchase. Dana is unequivocally the reason why I was able to purchase my home in Laguna Niguel and provide my family with a world-class community. Without her guidance and experience, I would still be in the market attempting to navigate the ever-changing work of real estate.</p>
    <p class="who">Marisol Quintero</p>
  </div>
  <div class="abs card" style="left:814px;top:526px;width:166px;height:241px;">
    <p>Dana is the kind of Real Estate professional everyone wants to represent them. She is knowledgeable, ethical, energetic, and follows up on every detail. <strong>Her honesty, integrity and expertise combined make her a very special and remarkable professional.</strong> We were lucky to find her!</p>
    <p class="who">Graham &amp; Nora Ellison</p>
  </div>
  <div class="abs card" style="left:987px;top:526px;width:167px;height:175px;">
    <p>Dana got us an amazing deal on our new home and sold our old home in a week. Dana is patient, hardworking, professional and most importantly HONEST. <strong>Dana is definitely one of the best in the business!</strong></p>
    <p class="who">Tessa &amp; Miles Corbin</p>
  </div>
</body>
</html>
```